Organic All Natural Gluten Free Dog Treat company needs a Design for our Label/Packaging.

We are a start up company making organic all natural gluten free dog biscuits. We are looking for a catchy label design that will impress upon first sight. Colors can be almost anything, some to consider are green, blue, white, beige, Black, Burgundy. We will be running a high class, high end business and really need to see concepts that reflect this. We are not really looking for anything comical or fun, however it needs to be nice to look at and look to be high end quality. The photo's that I have attached are what we like from other companies, these are just to throw around and maybe get ideas from. Our labels will be either 4" wide x 5" high or 5" wide x 6" high.
Updates

Project Deadline Extended Reason: We wish to extend 5 days as we would like to see more designs. Added Tuesday, July 7, 2015

Project Deadline Extended
Reason: Need more designs to make final decision.

Target Market(s)

Anyone who owns dog's or dog lover's.

Industry/Entity Type

It Company

Font styles to use
Serif
Sans Serif
Decorative
Script

Requirements
Must have
• "Stay Close Alwaystime" is the name of our business so it needs to be included,
• All Natural Organic Dog Treats...Gluten Free, No Preservatives, No Wheat, No Soy, Corn, or GMO's, Nothing Artificial, Baked by Stay Close AlwaysTime LLC., Dallas, TX.
• 6 oz., made in U.S.A.
• We don't need to use the logo, as long as the words "Stay Close AlwaysTime" are included.
Nice to have
• Not sure what colors we want, we would like to see a variety which can include brown, blue, black, green, red, yellow, orange, purple, beige, burgundy, white color scheme?? Maybe white or brownish, blueish background? American flag.
• We have uploaded a photo tilted American Eskimo Puppies for Label, we would like to have this included if possible. We have 4 flavors, Peanut Butter N' Honey, Pumpkin N' Spice, Sweet Potato, and Blueberry N' Coconut, maybe you can add the name and color code for one of these.

```html
<!DOCTYPE html>
<html lang="en">
<head>
<meta charset="utf-8">
<title>Stay Close AlwaysTime – Dog Treat Label</title>
<link rel="stylesheet" href="https://fonts.googleapis.com/css2?family=Kalam:wght@700&family=Roboto+Condensed:wght@700&family=Montserrat:wght@700&display=swap">
<style>
  :root {
    --rose: #ee6b7c;
    --sky: #33c4f2;
    --olive: #7e8f3b;
    --ink: #111111;
    --paper-light: #f1ece7;
    --paper-dark: #e2d8ce;
    --grass-light: #6fa83a;
    --grass-dark: #3f7a22;
    --rust: #d8613a;
    --white: #ffffff;
  }
  * { margin: 0; padding: 0; box-sizing: border-box; }
  html, body { width: 960px; height: 1200px; overflow: hidden; }
  body { background: var(--paper-light); }

  .label {
    position: relative;
    width: 960px;
    height: 1200px;
    background: linear-gradient(180deg, var(--paper-light) 0%, var(--paper-dark) 100%);
    overflow: hidden;
  }

  .masthead {
    position: absolute; left: 0; top: 0;
    width: 960px; height: 258px;
    background: var(--rose);
    display: flex;
    align-items: center;
    justify-content: center;
  }
  .brand-name {
    font-family: "Montserrat", sans-serif;
    font-weight: 700;
    font-size: 88px;
    line-height: 100px;
    letter-spacing: 2px;
    color: var(--sky);
    text-align: center;
  }

  .tagline {
    position: absolute; left: 27px; top: 313px;
    width: 906px; height: 64px;
    border-radius: 32px;
    background: var(--olive);
    color: var(--white);
    font-family: "Kalam", cursive;
    font-weight: 700;
    font-size: 46px;
    line-height: 70px;
    letter-spacing: 5px;
    text-align: center;
    white-space: nowrap;
  }

  .claims {
    list-style: none;
    font-family: "Roboto Condensed", sans-serif;
    font-weight: 700;
    color: var(--ink);
  }
  .claim {
    position: absolute;
    display: flex; align-items: center;
    white-space: nowrap;
    letter-spacing: 1px;
  }
  .claim svg { flex: none; }
  .claim--lead { left: 305px; top: 441px; font-size: 38px; gap: 16px; }
  .claim--lead svg { width: 36px; height: 36px; }
  .claim--item { font-size: 29px; gap: 13px; }
  .claim--item svg { width: 29px; height: 29px; }

  .col-a { left: 248px; }
  .col-b { left: 513px; }
  .row-1 { top: 508px; }
  .row-2 { top: 556px; }
  .row-3 { top: 600px; }

  .photo-band {
    position: absolute; left: 0; top: 683px;
    width: 960px; height: 283px;
    border: 3px solid var(--white);
    background: linear-gradient(180deg, var(--grass-light) 0%, var(--grass-dark) 100%);
  }
  .net-weight {
    position: absolute; left: 825px; top: 902px;
    width: 108px; height: 40px;
    border-radius: 20px;
    background: var(--rust);
    color: var(--ink);
    font-family: "Roboto Condensed", sans-serif;
    font-weight: 700;
    font-size: 34px;
    line-height: 40px;
    text-align: center;
  }

  .footer-band {
    position: absolute; left: 0; top: 1128px;
    width: 960px; height: 72px;
    background: var(--rose);
    color: var(--sky);
    font-family: "Montserrat", sans-serif;
    font-weight: 700;
    font-size: 27px;
    line-height: 74px;
    letter-spacing: 3px;
    text-align: center;
    white-space: nowrap;
  }
</style>
</head>
<body>
  <svg width="0" height="0" style="position:absolute" aria-hidden="true">
    <defs>
      <symbol id="tick-box" viewBox="0 0 30 30">
        <rect x="0" y="0" width="30" height="30" rx="5" fill="#111111"/>
        <path d="M7 15.5 L12.5 21 L23 9.5" fill="none" stroke="#ffffff" stroke-width="3.6" stroke-linecap="round" stroke-linejoin="round"/>
      </symbol>
    </defs>
  </svg>

  <main class="label">
    <header class="masthead">
      <h1 class="brand-name">Stay Close<br>AlwaysTime</h1>
    </header>

    <div class="tagline">All Natural Organic Dog Treats</div>

    <ul class="claims">
      <li class="claim claim--lead"><svg><use href="#tick-box"/></svg>Nothing Artificial</li>
      <li class="claim claim--item col-a row-1"><svg><use href="#tick-box"/></svg>Gluten Free</li>
      <li class="claim claim--item col-a row-2"><svg><use href="#tick-box"/></svg>No Wheat</li>
      <li class="claim claim--item col-a row-3"><svg><use href="#tick-box"/></svg>No Corn</li>
      <li class="claim claim--item col-b row-1"><svg><use href="#tick-box"/></svg>No Preservatives</li>
      <li class="claim claim--item col-b row-2"><svg><use href="#tick-box"/></svg>No Soy</li>
      <li class="claim claim--item col-b row-3"><svg><use href="#tick-box"/></svg>No GMO's</li>
    </ul>

    <div class="photo-band" role="img" aria-label="Photo of white fluffy puppies running in a line across green grass"></div>
    <div class="net-weight">6 oz</div>

    <footer class="footer-band">Baked by Stay Close AlwaysTime LLC</footer>
  </main>
</body>
</html>
```